Poster Needed for Church Conference

I need a poster for a weekend conference at my church. Looking to attract as many people as possible. We are a church in the suburbs of Houston. This is mainly for our own church members but we are opening it up to outside church members.

Please see previous design from last conference and all other graphic work that can (doesn't need to be) included.

Target Market(s)

It's targeted for all people. But our main audience is families. around the age of 30 should be main target.

Industry/Entity Type

Non-Profit

Font styles to use
Serif
Sans Serif

Colors

Designer to choose colors to be used in the design.

Requirements
Must have
• 11x17 design with ability to shrink and blow up. but ideally for 11x17
• Content and wording:
• "Rooted Lantern Conference: Bridging the gap between generations and passing on our deepest beliefs and values."
• Featuring Dr. Glen Marlowe. Author of "The Map of Q9"
• Aug 25-26: Friday 8-10 pm, Saturday 4-8 pm
• Cost Adults $15/Children $5: Covers admission to all sessions and workshops, refreshments and Saturday dinner. *kids 5 and under free
• Childcare provided for all sessions. "
• Please use church logo and address on flyer: 4312 Orchard Bend, Harlow Springs, TX 77512
Nice to have
• Ideally it will be designed so that we can crop a 16:9 pp announcement slide and header for our website.
Should not have
• anything offensive

```html
<!DOCTYPE html>
<html lang="en">
<head>
<meta charset="utf-8">
<title>Rooted Lantern Conference</title>
<link href="https://fonts.googleapis.com/css2?family=Sniglet:wght@800&family=Walter+Turncoat&family=Schoolbell&family=Oswald:wght@600&display=swap" rel="stylesheet">
<style>
  :root {
    --wood: #e6c7a0;
    --wood-dark: #dbb88d;
    --plank-line: rgba(160, 110, 60, 0.18);
    --title-blue: #4b87c8;
    --band-orange: #edb162;
    --band-orange-deep: #e9a54c;
    --tape-yellow: rgba(240, 238, 110, 0.78);
    --red: #ef5a5b;
    --green: #9acb3f;
    --charcoal: #2d2d2d;
    --name-green: #6cc24a;
    --ink: #2e2a25;
    --white: #ffffff;
    --hand: "Walter Turncoat", "Schoolbell", cursive;
  }
  * { box-sizing: border-box; margin: 0; padding: 0; }
  html, body { width: 776px; height: 1200px; overflow: hidden; }
  body { font-family: var(--hand); color: var(--ink); }

  .poster {
    position: relative;
    width: 776px;
    height: 1200px;
    overflow: hidden;
    background:
      repeating-linear-gradient(90deg, transparent 0 193px, var(--plank-line) 193px 195px),
      repeating-linear-gradient(0deg, rgba(255,255,255,0.05) 0 7px, rgba(150,100,50,0.04) 7px 13px),
      linear-gradient(135deg, var(--wood) 0%, var(--wood-dark) 100%);
  }

  .tape { position: absolute; background: var(--tape-yellow); height: 30px; }

  .title-card {
    position: absolute;
    left: 146px; top: 32px;
    width: 410px; height: 214px;
    background: var(--title-blue);
    transform: rotate(-1deg);
    display: flex; align-items: center; justify-content: center;
    text-align: center;
    box-shadow: 2px 3px 6px rgba(0,0,0,0.18);
  }
  .title-card h1 {
    font-family: "Sniglet", sans-serif;
    font-weight: 800;
    color: var(--white);
    font-size: 46px;
    line-height: 1.08;
  }

  .band { position: absolute; background: var(--band-orange); display: flex; align-items: center; }
  .tagline-band {
    left: 30px; top: 305px; width: 700px; height: 84px;
    justify-content: center; text-align: center;
    font-size: 21px; line-height: 1.35;
  }
  .speaker-band {
    left: 26px; top: 410px; width: 444px; height: 68px;
    padding-left: 66px;
    font-size: 19px; line-height: 1.3;
    clip-path: polygon(0 0, 100% 0, 96% 50%, 100% 100%, 0 100%, 3% 50%);
  }

  .speaker-photo {
    position: absolute;
    left: 42px; top: 506px;
    width: 340px; height: 322px;
    background: radial-gradient(circle at 50% 45%, #c79a80 0%, #8a6452 35%, #1d1a18 70%);
    border: 3px solid var(--band-orange-deep);
    transform: rotate(-1.5deg);
  }

  .event-card {
    position: absolute;
    left: 440px; top: 440px;
    width: 305px; height: 390px;
    background: var(--red);
    padding: 26px 20px;
    transform: rotate(0.6deg);
    color: var(--white);
  }
  .event-card .date { font-family: "Sniglet", sans-serif; font-weight: 800; font-size: 23px; margin-bottom: 12px; }
  .event-card .session { font-size: 22px; line-height: 1.4; margin-bottom: 10px; }
  .event-card .cost-label { font-family: "Sniglet", sans-serif; font-weight: 800; font-size: 27px; margin: 18px 0 14px 76px; }
  .event-card .price { font-size: 22px; line-height: 1.45; margin-left: 76px; }

  .church-card {
    position: absolute;
    left: 80px; top: 862px;
    width: 266px; height: 302px;
    background: var(--charcoal);
    color: var(--white);
    transform: rotate(-1.5deg);
    padding: 70px 0 0 36px;
  }
  .church-name {
    display: flex; align-items: center; gap: 12px;
    font-family: var(--hand);
    font-size: 34px; color: var(--name-green);
    margin-bottom: 70px;
  }
  .church-name .mark { width: 22px; height: 22px; border-radius: 50%; background: var(--name-green); }
  .church-card address { font-style: normal; font-family: var(--hand); font-size: 15px; line-height: 1.5; }

  .childcare-card {
    position: absolute;
    left: 416px; top: 862px;
    width: 284px; height: 222px;
    background: var(--green);
    padding: 40px 16px 0 16px;
    transform: rotate(0.8deg);
  }
  .childcare-card h2 { font-weight: 400; font-size: 19px; line-height: 1.3; margin-bottom: 18px; }
  .childcare-card p { font-family: "Oswald", sans-serif; font-weight: 600; font-size: 13px; line-height: 1.35; }

  .web-band {
    left: 395px; top: 1116px; width: 326px; height: 48px;
    justify-content: center;
    font-family: "Oswald", sans-serif; font-weight: 600;
    font-size: 21px; letter-spacing: 0.5px;
    clip-path: polygon(3% 0, 100% 0, 98% 50%, 100% 100%, 0 100%, 2% 50%);
  }
</style>
</head>
<body>
<main class="poster">
  <section class="title-card"><h1>ROOTED LANTERN<br>CONFERENCE</h1></section>
  <div class="tape" style="left:340px;top:8px;width:58px;height:58px;"></div>

  <div class="band tagline-band">Bridging the gap between generations and passing<br>on our deepest beliefs and values.</div>
  <div class="band speaker-band">Featuring Dr. Glen Marlowe.<br>Author of "The Map of Q9</div>

  <div class="speaker-photo" role="img" aria-label="Portrait photo of the featured speaker"></div>
  <div class="tape" style="left:40px;top:520px;width:120px;transform:rotate(-40deg);"></div>
  <div class="tape" style="left:290px;top:760px;width:140px;transform:rotate(-40deg);"></div>

  <section class="event-card">
    <div class="date">AUGUST 25-26, 2017</div>
    <div class="session">Friday<br>8-10 pm</div>
    <div class="session">Saturday<br>&nbsp;4-8 pm</div>
    <div class="cost-label">COST:</div>
    <div class="price">Adults $15<br>Children $5</div>
  </section>
  <div class="tape" style="left:735px;top:540px;width:42px;height:170px;background:var(--band-orange-deep);opacity:.9;"></div>

  <section class="church-card">
    <div class="church-name"><span class="mark"></span>Grace Vale</div>
    <address>4312 Orchard Bend,<br>Harlow Springs, TX 77512</address>
  </section>
  <div class="tape" style="left:70px;top:900px;width:110px;transform:rotate(-38deg);"></div>

  <section class="childcare-card">
    <h2>Childcare provided<br>&nbsp;for all sessions.</h2>
    <p>Covers admission to all sessions<br>and workshops, refreshments<br>and Saturday dinner.<br>*kids 5 and under free</p>
  </section>
  <div class="tape" style="left:490px;top:838px;width:90px;height:42px;"></div>

  <div class="band web-band">www.gracevale.org</div>
</main>
</body>
</html>
```